Business Cards

I'm an contractor and consultant in IT Project management. I'd like a design for business cards.
In my work I mostly meet clients, peer project managers and technical staff. I usually exchange business cards at technical conventions or when networking.
I provide services that are:
- Updated, always with a fresh look on technology
- Solid and reliable
- Flexible schedule and always available
The current business card has been attached to provide information.
Target Market(s)
IT managers, IT project managers, consultants, recruitment staff. Age 30-45 years. College/University degree.
Industry/Entity Type
Contractor
Colors
Designer to choose colors to be used in the design.
Requirements
Must have
- Two sides, one side with personal information and the other side with company name.
Text in Norwegian, including Norwegian characters
Nice to have
- It should be possible for non-Norwegian speakers to read the contact details.

```html
<!DOCTYPE html>
<html lang="no">
<head>
<meta charset="utf-8">
<title>Fjellvik Consulting AS – Visittkort</title>
<link href="https://fonts.googleapis.com/css2?family=Libre+Bodoni:wght@400;600;700&display=swap" rel="stylesheet">
<style>
  :root {
    --backdrop: #2f2f0e;
    --paper: #ffffff;
    --brand-blue: #2a9fd0;
    --band-grey: #7f8f8f;
    --ink: #1f1f1f;
    --muted-grey: #8a8a8a;
    --on-blue: #ffffff;
  }
  * { margin: 0; padding: 0; box-sizing: border-box; }
  html, body {
    width: 1200px; height: 1000px; overflow: hidden;
    background: var(--backdrop);
    font-family: "Libre Bodoni", "Bodoni 72", Georgia, serif;
  }
  .canvas { position: relative; width: 1200px; height: 1000px; }

  .card {
    position: absolute; left: 250px; width: 700px; height: 390px;
    background: var(--paper); overflow: hidden;
    box-shadow: 0 8px 24px rgba(0,0,0,.35);
  }
  .card--front { top: 70px; }
  .card--back { top: 540px; }

  .card__band { position: absolute; left: 0; right: 0; background: var(--band-grey); }
  .card__panel { position: absolute; left: 0; right: 0; bottom: 0; background: var(--brand-blue); }

  .card--front .card__band { top: 200px; height: 16px; }
  .card--front .card__panel { top: 216px; }

  .front__company {
    position: absolute; left: 100px; top: 136px;
    font-size: 46px; font-weight: 400; letter-spacing: 4px;
    color: var(--brand-blue); white-space: nowrap;
  }
  .front__tagline {
    position: absolute; left: 200px; top: 196px;
    font-size: 23px; font-weight: 600; letter-spacing: 2px;
    color: var(--ink); white-space: nowrap;
  }
  .front__web {
    position: absolute; left: 170px; bottom: 34px;
    font-size: 19px; font-weight: 600; letter-spacing: 2.5px;
    color: var(--on-blue);
  }

  .card--back .card__band { top: 236px; height: 16px; }
  .card--back .card__panel { top: 252px; }

  .back__company {
    position: absolute; left: 0; top: 160px; width: 320px; text-align: center;
    font-size: 26px; letter-spacing: 2px; color: var(--muted-grey);
  }
  .back__tagline {
    position: absolute; left: 0; top: 199px; width: 320px; text-align: center;
    font-size: 19px; letter-spacing: 1.5px; color: var(--muted-grey);
  }
  .back__name {
    position: absolute; left: 380px; top: 156px; width: 300px; text-align: center;
    font-size: 34px; letter-spacing: 3px; color: var(--brand-blue);
    font-variant: small-caps;
  }
  .back__role {
    position: absolute; left: 380px; top: 198px; width: 300px; text-align: center;
    font-size: 19px; font-weight: 700; letter-spacing: 2px; color: var(--ink);
  }
  .back__contact {
    position: absolute; left: 0; top: 266px; width: 640px; text-align: center;
    color: var(--on-blue); font-weight: 600; letter-spacing: 1.5px;
    font-size: 16px; line-height: 23px; font-style: normal;
  }
  .back__contact .contact__web { font-size: 20px; letter-spacing: 2px; }
</style>
</head>
<body>
  <main class="canvas">
    <section class="card card--front" aria-label="Forside">
      <div class="card__band"></div>
      <div class="card__panel"></div>
      <h1 class="front__company">Fjellvik Consulting AS</h1>
      <p class="front__tagline">IT Implementering</p>
      <p class="front__web">www.fjellvikconsulting.no</p>
    </section>

    <section class="card card--back" aria-label="Bakside">
      <div class="card__band"></div>
      <div class="card__panel"></div>
      <p class="back__company">Fjellvik Consulting AS</p>
      <p class="back__tagline">IT Implementering</p>
      <h2 class="back__name">Eirik Åsland</h2>
      <p class="back__role">IT Rådgiver</p>
      <address class="back__contact">
        Bjørnstads gate 14<br>
        0461 OSLO<br>
        Mob.: 91234567<br>
        eirik@fjellvikconsulting.no<br>
        <span class="contact__web">www.fjellvikconsulting.no</span>
      </address>
    </section>
  </main>
</body>
</html>
```